RW Business Card Design

My company provides advising/training and coaching services to business owners who want better financial results and better work/life balance. We help them through creating custom plans supported with education, strategic thinking and accountability.

We also help through some online courses which are geared to smaller businesses.
Updates

please also include our nth american contact # +1 555 208 4471

Industry/Entity Type

Financial

Contact Information for Business Card

Morgan Halberd
morgan@morganhalberd-example.com
+61 400 555 917
www.morganhalberd-example.com

```html
<!DOCTYPE html>
<html lang="en">
<head>
<meta charset="utf-8">
<title>Morgan Halberd Business Card</title>
<link rel="stylesheet" href="https://fonts.googleapis.com/css2?family=Lato:wght@300;400;700;900&display=swap">
<style>
  :root {
    --bg: #e9e6e1;
    --white: #ffffff;
    --slate: #4a4b4f;
    --slate-text: #ececec;
    --muted: #c9c9c9;
    --blue: #1f72c2;
    --brand-blue: #1d6fb8;
    --gold: #f3b41b;
    --grey-circle: #e3e3e3;
  }
  * { box-sizing: border-box; margin: 0; padding: 0; }
  html, body { width: 1200px; height: 1100px; overflow: hidden; }
  body { background: var(--bg); font-family: "Lato", sans-serif; position: relative; }

  .card { position: absolute; width: 698px; height: 421px; box-shadow: 0 6px 18px rgba(0,0,0,.25); overflow: hidden; }

  /* Front */
  .card-front { left: 60px; top: 70px; background: var(--slate); }
  .front-top { position: absolute; left: 0; top: 0; width: 100%; height: 182px; background: var(--white); }
  .brand-mark { position: absolute; left: 52px; top: 46px; width: 88px; height: 88px; border-radius: 50%; background: var(--brand-blue); }
  .brand-name { position: absolute; left: 170px; top: 62px; font-size: 50px; font-weight: 400; letter-spacing: -0.5px; color: var(--brand-blue); }
  .social-row { position: absolute; right: 34px; top: 124px; display: flex; gap: 22px; }
  .social-row span { width: 42px; height: 42px; border-radius: 50%; background: var(--grey-circle); }

  .contact-list { position: absolute; left: 24px; top: 250px; list-style: none; }
  .contact-list li { display: flex; align-items: center; gap: 8px; height: 30px; font-size: 19.5px; font-weight: 700; color: var(--slate-text); }
  .contact-list svg { width: 14px; height: 16px; flex: none; }

  .person { position: absolute; right: 26px; top: 244px; text-align: right; }
  .person-name { font-size: 26px; font-weight: 400; color: var(--white); }
  .person-role { font-size: 13px; font-weight: 700; letter-spacing: .5px; color: var(--gold); margin-top: 2px; }
  .person-address { margin-top: 44px; font-size: 18px; line-height: 30px; color: var(--muted); text-align: center; }

  /* Back */
  .card-back { left: 440px; top: 620px; background: var(--blue); color: var(--white); }
  .tagline { position: absolute; left: 34px; top: 36px; font-size: 27px; font-weight: 400; line-height: 31px; text-transform: uppercase; }
  .tagline .accent { color: var(--gold); }
  .benefits { position: absolute; left: 40px; top: 168px; list-style: none; }
  .benefits li { display: flex; align-items: center; gap: 22px; height: 64px; font-size: 25px; font-weight: 700; color: #f1f4f8; }
  .benefits svg { width: 38px; height: 38px; flex: none; }
  .back-url { position: absolute; left: 0; right: 0; bottom: 30px; text-align: center; font-size: 28px; font-weight: 700; }
  .back-url .accent { color: var(--gold); }
</style>
</head>
<body>

<section class="card card-front">
  <div class="front-top">
    <div class="brand-mark"></div>
    <div class="brand-name">MORGANHALBERD</div>
    <div class="social-row"><span></span><span></span><span></span><span></span></div>
  </div>

  <ul class="contact-list">
    <li><svg viewBox="0 0 14 16"><rect x="3" y="1" width="8" height="14" rx="2" fill="#f3b41b"/></svg>Australia&nbsp; +61 2 5550 3182</li>
    <li><svg viewBox="0 0 14 16"><rect x="3" y="1" width="8" height="14" rx="2" fill="#f3b41b"/></svg>North America&nbsp; +1 555 208 4471</li>
    <li><svg viewBox="0 0 14 16"><rect x="3" y="1" width="8" height="14" rx="2" fill="none" stroke="#f3b41b" stroke-width="1.6"/></svg>Mobile&nbsp; 0400 555 917</li>
    <li><svg viewBox="0 0 14 16"><rect x="1" y="4" width="12" height="9" fill="#f3b41b"/><path d="M1 4 L7 9 L13 4" fill="none" stroke="#4a4b4f" stroke-width="1.2"/></svg>morgan@morganhalberd-example.com</li>
    <li><svg viewBox="0 0 14 16"><circle cx="7" cy="8" r="6" fill="#f3b41b"/><path d="M1 8 H13 M7 2 V14" stroke="#4a4b4f" stroke-width="1.1"/></svg>www.morganhalberd-example.com</li>
  </ul>

  <div class="person">
    <div class="person-name">Morgan Halberd</div>
    <div class="person-role">BUSINESS COACH</div>
    <div class="person-address">14 Willowmere Lane<br>Brookhaven, NSW 2999</div>
  </div>
</section>

<section class="card card-back">
  <h2 class="tagline">We help<br><span class="accent">business owners</span><br>get their life back...</h2>

  <ul class="benefits">
    <li><svg viewBox="0 0 38 38"><circle cx="19" cy="19" r="15" fill="none" stroke="#f3b41b" stroke-width="3.5"/><path d="M19 10 V19 L25 23" fill="none" stroke="#f3b41b" stroke-width="3" stroke-linecap="round"/></svg>Get More Time &amp; Freedom From Your Business</li>
    <li><svg viewBox="0 0 38 38"><path d="M14 6 H24 L21 11 H17 Z" fill="#f3b41b"/><circle cx="19" cy="23" r="13" fill="#f3b41b"/><text x="19" y="29" text-anchor="middle" font-family="Lato, sans-serif" font-weight="900" font-size="16" fill="#1f72c2">$</text></svg>Grow Your Profits And Have Better Cash Flow</li>
    <li><svg viewBox="0 0 38 38"><circle cx="12" cy="12" r="6" fill="#f3b41b"/><circle cx="26" cy="12" r="6" fill="#f3b41b"/><path d="M2 34 Q2 20 12 20 Q22 20 22 34 Z M16 34 Q16 20 26 20 Q36 20 36 34 Z" fill="#f3b41b"/></svg>Train A Team That Can Think Like You</li>
  </ul>

  <div class="back-url">www.<span class="accent">morganhalberd</span>-example.com</div>
</section>

</body>
</html>
```